Book Cover needed - Disinformation and fake news

I need a book cover (front, back, spine) for the 1st edition of a book entitled ‘Marea Silenciosa’ (Means – Silent Tide) and subtitled ‘Los ecos que nadie quiso escuchar’ (Means - The echoes nobody wanted to hear) (inverted commas not to be part of the title and subtitle). The author is ‘Tomás Herreruela’. The finished size of the paperback version will be 5.25" x 8". There will be paperback and e-book versions, so 2 covers will need to be provided: one for the e-book version just with the front cover, and the full book cover for the paperback version.
The final number of pages is expected to be in the region of 350-500 pages. Text for the back cover is down below, and at the bottom of the back cover should have space for the ISBN bar code on the right. The books will be published with PQN - Velmora, so should follow their indications for any specification needed.
The topics discussed include disinformation, fake news, psychological operations. Feel free to design the cover based on those. The design should be original and not include any stock images that have been created by someone else or may require obtaining a copyright license to use.
Back Cover Text (spacing should be respected) :
Oficina del consenso, desinformación, “fake news”... en los últimos años nos hemos visto envueltos en una discusión pública rodeados de estos términos sin terminar de entender exactamente qué significan y lo que es peor, sin saber que realmente nos rodean desde que el hombre es hombre.
En esta obra el autor busca acercanos al mundo de la Marea Silenciosa, aquellas operaciones que buscan influir sobre el comportamiento de la población. Sin hacer uso de un lenguaje excesivamente técnico relata como la evolución de la naturaleza de la guerra a los parámetros del siglo XXI promueve un enfoque del conflicto que no supone un uso de la fuerza tradicional. ¿Para qué atacar las instituciones de un país de forma directa, cuando puedes fomentar el conflicto social entre grupos antagónicos y desestabilizar sin realizar un solo disparo?
¿Cómo razona el ser humano? ¿Son nuestras ideas tan nuestras como creemos? ¿Por qué importa tanto el uso preciso del lenguaje a la hora de comunicarnos?, ¿Cómo nos afectan las razones y emociones de los demás? ¿Por qué tendemos a prestar mayor atención a argumentos que encajen con nuestras propias ideas? ¿Cómo nos afecta la conversación en redes sociales?
Armados con el conocimiento que reside en este libro, quizás, seamos menos susceptibles de caer bajo la influencia de grupos con intereses espurios.
General public with an interest on disinformation - fake news

```html
<!DOCTYPE html>
<html lang="es">
<head>
<meta charset="utf-8">
<title>Marea Silenciosa — Cubierta</title>
<link rel="stylesheet" href="https://fonts.googleapis.com/css2?family=Oswald:wght@300;400&family=Open+Sans:wght@400&display=swap">
<style>
  :root {
    --page-bg: #f1f1f1;
    --cover-bg: #2b2b2b;
    --ink-light: #ffffff;
    --ink-dark: #1f1f1f;
    --title-top: #6a6a6a;
    --art-light: #e9e9e9;
    --art-mid: #bdbdbd;
  }
  * { margin: 0; padding: 0; box-sizing: border-box; }
  html, body { width: 899px; height: 1200px; overflow: hidden; }
  body { background: var(--page-bg); position: relative; }

  .cover-spread {
    position: absolute; left: 0; top: 290px;
    width: 899px; height: 620px;
    background: var(--cover-bg);
    color: var(--ink-light);
    overflow: hidden;
  }

  .title-line {
    position: absolute;
    font-family: "Oswald", sans-serif;
    font-weight: 300;
    line-height: 1;
    white-space: nowrap;
    background: linear-gradient(to bottom, var(--title-top) 0%, var(--ink-light) 80%);
    -webkit-background-clip: text;
    background-clip: text;
    color: transparent;
  }
  .title-line.second { background: none; color: var(--ink-light); }

  /* Back cover */
  .back-title-main { left: 118px; top: 58px; font-size: 50px; letter-spacing: 1px; }
  .back-title-sub  { left: 118px; top: 110px; font-size: 38px; letter-spacing: 0.5px; }

  .back-blurb {
    position: absolute; left: 60px; top: 170px; width: 312px;
    font-family: "Open Sans", sans-serif;
    font-size: 9.6px; line-height: 1.4;
    text-align: justify; hyphens: auto;
  }
  .back-blurb p + p { margin-top: 13px; }

  .isbn-space {
    position: absolute; left: 60px; top: 510px;
    width: 100px; height: 60px;
    background: var(--ink-light);
  }

  /* Spine */
  .spine-title {
    position: absolute; left: 436px; top: 72px;
    writing-mode: vertical-rl;
    font-family: "Oswald", sans-serif; font-weight: 300;
    font-size: 29px; letter-spacing: 0.5px; white-space: nowrap;
  }
  .spine-author {
    position: absolute; left: 424px; top: 342px;
    writing-mode: vertical-rl;
    font-family: "Oswald", sans-serif; font-weight: 400;
    font-size: 11px; letter-spacing: 11px; white-space: nowrap;
  }

  /* Front cover */
  .front-title-main { left: 502px; top: 38px; font-size: 106px; letter-spacing: 2px; }
  .front-title-sub  { left: 504px; top: 150px; font-size: 66px; letter-spacing: 1px; }

  .front-artwork {
    position: absolute; left: 512px; top: 236px;
    width: 387px; height: 258px;
  }

  .subtitle-band {
    position: absolute; left: 560px; top: 520px;
    width: 339px; height: 36px;
    background: var(--ink-light);
    display: flex; align-items: center; padding-left: 12px;
    font-family: "Oswald", sans-serif; font-weight: 400;
    font-size: 16.5px; color: var(--ink-dark); white-space: nowrap;
  }

  .front-author {
    position: absolute; left: 588px; top: 570px;
    font-family: "Oswald", sans-serif; font-weight: 400;
    font-size: 14px; letter-spacing: 12.5px; white-space: nowrap;
  }
</style>
</head>
<body>
  <section class="cover-spread">
    <!-- Back cover -->
    <h2 class="title-line back-title-main">MAREA</h2>
    <h2 class="title-line second back-title-sub">SILENCIOSA</h2>

    <div class="back-blurb">
      <p>Oficina del consenso, desinformación, “fake news”... en los últimos años nos hemos visto envueltos en una discusión pública rodeados de estos términos sin terminar de entender exactamente qué significan y lo que es peor, sin saber que realmente nos rodean desde que el hombre es hombre.</p>
      <p>En esta obra el autor busca acercanos al mundo de la Marea Silenciosa, aquellas operaciones que buscan influir sobre el comportamiento de la población. Sin hacer uso de un lenguaje excesivamente técnico relata como la evolución de la naturaleza de la guerra a los parámetros del siglo XXI promueve un enfoque del conflicto que no supone un uso de la fuerza tradicional. ¿Para qué atacar las instituciones de un país de forma directa, cuando puedes fomentar el conflicto social entre grupos antagónicos y desestabilizar sin realizar un solo disparo?</p>
      <p>¿Cómo razona el ser humano? ¿Son nuestras ideas tan nuestras como creemos? ¿Por qué importa tanto el uso preciso del lenguaje a la hora de comunicarnos?, ¿Cómo nos afectan las razones y emociones de los demás? ¿Por qué tendemos a prestar mayor atención a argumentos que encajen con nuestras propias ideas? ¿Cómo nos afecta la conversación en redes sociales?</p>
    </div>

    <div class="isbn-space"></div>

    <!-- Spine -->
    <div class="spine-title">MAREA SILENCIOSA</div>
    <div class="spine-author">TOMÁS HERRERUELA</div>

    <!-- Front cover -->
    <h1 class="title-line front-title-main">MAREA</h1>
    <h1 class="title-line second front-title-sub">SILENCIOSA</h1>

    <svg class="front-artwork" viewBox="0 0 387 258" role="img" aria-label="Illustration: white profile silhouette of a head with a tangled line scribble for a brain and tangled lines flowing from the mouth">
      <defs>
        <radialGradient id="artGlow" cx="50%" cy="50%" r="60%">
          <stop offset="0%" stop-color="var(--art-light)"/>
          <stop offset="100%" stop-color="var(--art-mid)" stop-opacity="0.35"/>
        </radialGradient>
      </defs>
      <rect x="0" y="0" width="387" height="258" fill="url(#artGlow)"/>
    </svg>

    <div class="subtitle-band">LOS ECOS QUE NADIE QUISO ESCUCHAR</div>
    <div class="front-author">TOMÁS HERRERUELA</div>
  </section>
</body>
</html>
```